Stationery Design Project - Ma clairiere

We are a french company, Ma Clairiere. It means My Glade.
We own and manage woods, we transform it industrially into very high quality (dry) logs and pellets and we commercialize them to individuals in France.
People can order the logs online or by phone and get the wood logs delivered at home.

After our great logo contest, we would like to launch a new stationery project.
Updates

Target Market(s)

inhabitants of sub-urban areas in France. (living in houses not in apartment )

Industry/Entity Type

It Company

Requirements
Must have
• content see attachment
logo

For the business card, we would like on the front side, the logo, name + contact info. We would like to use the back side for commercial purpose insisting on our distinctive value proposition.
Nice to have
• the back side of the business card can be more colorful

```html
<!DOCTYPE html>
<html lang="fr">
<head>
<meta charset="utf-8">
<title>Ma Clairiere – Carte de visite</title>
<link href="https://fonts.googleapis.com/css2?family=Montserrat:wght@400;500;600;700;800&display=swap" rel="stylesheet">
<style>
  :root {
    --red: #c4161c;
    --red-deep: #9e0d12;
    --red-soft: #d9463f;
    --red-mist: #cf5a4e;
    --grey-dark: #3b3b3b;
    --grey-mid: #5a5a5a;
    --paper: #f7f7f7;
    --paper-shade: #e9e3e1;
    --white: #ffffff;
    --stage: #e4e4e4;
  }
  * { box-sizing: border-box; margin: 0; padding: 0; }
  html, body { width: 1200px; height: 900px; overflow: hidden; }
  body {
    background: var(--stage);
    font-family: "Montserrat", Arial, sans-serif;
    display: flex;
    flex-direction: column;
    align-items: center;
    justify-content: center;
    gap: 36px;
  }
  .card {
    position: relative;
    width: 700px;
    height: 400px;
    overflow: hidden;
    box-shadow: 0 6px 18px rgba(0,0,0,.18);
  }

  /* Back side */
  .card--back {
    background: radial-gradient(circle at 70% 30%, var(--red-soft) 0%, var(--red) 45%, var(--red-deep) 100%);
    color: var(--white);
  }
  .back__illustration {
    position: absolute;
    right: 30px;
    top: 20px;
    width: 330px;
    height: 380px;
    background: radial-gradient(ellipse at 50% 45%, var(--red-mist) 0%, rgba(207,90,78,.4) 55%, rgba(207,90,78,0) 80%);
  }
  .back__brand {
    position: absolute;
    left: 48px;
    top: 150px;
    font-size: 26px;
    font-weight: 800;
    letter-spacing: -.5px;
  }
  .back__offer {
    position: absolute;
    left: 48px;
    top: 240px;
    width: 330px;
    font-size: 12.5px;
    line-height: 1.45;
    font-weight: 400;
  }
  .back__offer strong { font-weight: 700; }
  .back__order { margin-top: 14px; }
  .back__note {
    margin-top: 10px;
    font-size: 9px;
    opacity: .85;
  }

  /* Front side */
  .card--front { background: var(--paper); }
  .front__name {
    position: absolute;
    left: 48px;
    top: 110px;
    font-size: 16px;
    font-weight: 700;
    color: #222;
  }
  .front__brand {
    position: absolute;
    left: 46px;
    top: 165px;
    font-size: 36px;
    font-weight: 800;
    letter-spacing: -1.5px;
    color: var(--red);
  }
  .front__contacts {
    position: absolute;
    left: 48px;
    top: 222px;
    list-style: none;
    font-size: 14px;
    font-weight: 500;
    color: var(--grey-dark);
    line-height: 1.35;
  }
  .front__contacts li { display: flex; align-items: center; gap: 8px; }
  .front__contacts svg { width: 12px; height: 12px; fill: var(--red); }
  .front__illustration {
    position: absolute;
    right: 90px;
    top: 36px;
    width: 160px;
    height: 250px;
    background: radial-gradient(ellipse at 50% 50%, var(--paper-shade) 0%, rgba(233,227,225,0) 75%);
  }
  .front__band { position: absolute; left: 0; bottom: 0; width: 700px; height: 110px; }
  .front__web {
    position: absolute;
    right: 32px;
    bottom: 56px;
    display: flex;
    align-items: center;
    gap: 8px;
    color: var(--white);
    font-size: 14px;
    line-height: 1;
  }
  .front__web strong { font-weight: 700; }
  .front__web svg { width: 16px; height: 16px; }
</style>
</head>
<body>

  <section class="card card--back" aria-label="Verso de la carte">
    <div class="back__illustration" role="img" aria-label="Illustration d'un bûcheron en chemise à carreaux portant un plateau de bûches"></div>
    <div class="back__brand">Ma Clairiere</div>
    <div class="back__offer">
      <p><strong>Livraison gratuite</strong> de bois de chauffage à <strong>Lyon</strong><br>et sa région. Bûches, granulés, briquettes</p>
      <p class="back__order">Commandez sur<br><strong>www.maclairiere.fr</strong><br>ou au <strong>04 72 00 41 18</strong></p>
      <p class="back__note">Qualité supérieure, origine régionale certifiée, livraison en 48h</p>
    </div>
  </section>

  <section class="card card--front" aria-label="Recto de la carte">
    <div class="front__illustration" role="img" aria-label="Illustration d'un bûcheron debout tenant des bûches"></div>
    <div class="front__name">Lucien MARCHAND</div>
    <div class="front__brand">Ma Clairiere</div>
    <ul class="front__contacts">
      <li><svg viewBox="0 0 12 12" aria-hidden="true"><path d="M1 4c0-2 1-3 3-3h4c2 0 3 1 3 3H8.5L8 3H4l-.5 1zM2 5h8l1 6H1z"/></svg>04 72 00 41 18</li>
      <li><svg viewBox="0 0 12 12" aria-hidden="true"><rect x="3" y="0.5" width="6" height="11" rx="1.2"/><rect x="4" y="2" width="4" height="6" fill="#f7f7f7"/></svg>04 72 00 41 19</li>
      <li><svg viewBox="0 0 12 12" aria-hidden="true"><rect x="0.5" y="2" width="11" height="8" rx="1"/><path d="M1 3l5 4 5-4" stroke="#f7f7f7" stroke-width="1" fill="none"/></svg>marchand@maclairiere.fr</li>
    </ul>

    <svg class="front__band" viewBox="0 0 700 110" preserveAspectRatio="none" aria-hidden="true">
      <path d="M0 62 H350 C390 62 395 22 440 22 H700 V110 H0 Z" fill="var(--red)"/>
      <path d="M0 80 H700 V96 H0 Z" fill="var(--grey-mid)"/>
      <path d="M0 96 H700 V110 H0 Z" fill="var(--red-deep)"/>
    </svg>
    <div class="front__web">
      <svg viewBox="0 0 16 16" aria-hidden="true" fill="none" stroke="#fff" stroke-width="1.2"><circle cx="8" cy="8" r="7"/><ellipse cx="8" cy="8" rx="3" ry="7"/><path d="M1 8h14M2.5 4.5h11M2.5 11.5h11"/></svg>
      <span>www.<strong>maclairiere</strong>.fr</span>
    </div>
  </section>

</body>
</html>
```